Marlow Hire Business Card for recruitment company

We are looking for a Business Card Design that incorporates our personal details and our busines name and logo. We are a specialized search consultancy that recruit Property and Construction professionals.
We would like a business card that stands out and is appealing to the Construction and Property industry as well.

Target Market(s)

people in the construction and property industry

Contact Information for Business Card

Business Name and logo

Font styles to use
Serif

Colors
0094D4
00A9DD
6FCCEA
C7EBF8
E9F6FB

Requirements
Must have
• Business name and logo as well as contact details
Should not have
• No photos of us please

```html
<!DOCTYPE html>
<html lang="en">
<head>
<meta charset="utf-8">
<title>Marlow Hire – Business Card</title>
<link href="https://fonts.googleapis.com/css2?family=Roboto:wght@300;400;500;700&display=swap" rel="stylesheet">
<style>
  :root {
    --navy: #033d52;
    --navy-deep: #02364a;
    --white: #ffffff;
    --stage-grey: #8e8b87;
    --page-white: #ffffff;
    --rule: rgba(255,255,255,0.85);
  }
  * { margin: 0; padding: 0; box-sizing: border-box; }
  html, body { width: 1200px; height: 2643px; overflow: hidden; background: var(--page-white); }
  body { position: relative; font-family: 'Roboto', Arial, sans-serif; }

  .stage { position: absolute; left: 0; top: 0; width: 1200px; height: 900px; background: var(--stage-grey); }

  .card {
    position: absolute; width: 409px; height: 717px; overflow: hidden;
    background: var(--navy); color: var(--white);
    box-shadow: 0 6px 14px rgba(0,0,0,0.35);
    transform-origin: top left;
  }
  .card--small { transform: scale(0.738); }

  /* Front */
  .front-halo {
    position: absolute; left: 29px; top: -90px; width: 360px; height: 360px; border-radius: 50%;
    background: radial-gradient(circle, var(--navy) 55%, var(--navy-deep) 100%);
    opacity: 0.9;
  }
  .front-name {
    position: absolute; left: 0; right: 0; top: 330px; text-align: center;
    font-weight: 300; font-size: 46px; letter-spacing: 1px; text-transform: uppercase;
  }
  .front-web {
    position: absolute; left: 0; right: 0; top: 630px; text-align: center;
    font-weight: 400; font-size: 22px; letter-spacing: 1.2px;
  }

  /* Back */
  .back-top { position: absolute; left: 0; top: 0; width: 100%; height: 194px; background: var(--white); }
  .back-mark {
    position: absolute; left: 55px; top: 145px; width: 104px; height: 104px; border-radius: 50%;
    border: 5px solid var(--white); background: var(--navy);
    display: flex; align-items: center; justify-content: center;
    font-weight: 500; font-size: 13px; letter-spacing: 0.5px; text-transform: uppercase; text-align: center; line-height: 1.2;
  }
  .holder-name { position: absolute; left: 57px; top: 350px; font-weight: 700; font-size: 27px; }
  .holder-role { position: absolute; left: 57px; top: 386px; font-weight: 400; font-size: 17.5px; }
  .divider { position: absolute; left: 58px; top: 464px; width: 226px; height: 1.5px; background: var(--rule); }
  .social { position: absolute; top: 451px; width: 27px; height: 27px; border-radius: 50%; background: var(--white); }
  .social--one { left: 297px; }
  .social--two { left: 333px; }

  .contact-list { position: absolute; left: 57px; top: 524px; list-style: none; }
  .contact-item { display: flex; align-items: flex-start; font-weight: 500; font-size: 18px; line-height: 22px; margin-bottom: 10px; }
  .contact-item svg { flex: none; width: 26px; height: 26px; margin-right: 17px; margin-top: -2px; }
</style>
</head>
<body>

<section class="stage">
  <article class="card card--small" style="left:241px; top:189px;">
    <div class="front-halo"></div>
    <div class="front-name">Marlow Hire</div>
    <div class="front-web">www.marlowhire.nz</div>
  </article>

  <article class="card card--small" style="left:627px; top:161px;">
    <div class="back-top"></div>
    <div class="back-mark">Marlow<br>Hire</div>
    <div class="holder-name">Clara Whitfield</div>
    <div class="holder-role">Director | Senior Search Consultant</div>
    <div class="divider"></div>
    <span class="social social--one"></span><span class="social social--two"></span>
    <ul class="contact-list">
      <li class="contact-item"><svg viewBox="0 0 26 26"><circle cx="13" cy="13" r="11" fill="none" stroke="#fff" stroke-width="1.6"/><path d="M9 8l2 0 1 3-1.3 1a6 6 0 0 0 3 3l1-1.3 3 1v2a1.5 1.5 0 0 1-1.6 1.4A9 9 0 0 1 7.7 9.6 1.5 1.5 0 0 1 9 8z" fill="#fff"/></svg>+64 27 555 0142</li>
      <li class="contact-item"><svg viewBox="0 0 26 26"><circle cx="13" cy="13" r="11" fill="none" stroke="#fff" stroke-width="1.6"/><path d="M13 6.5a4.5 4.5 0 0 0-4.5 4.5c0 3.4 4.5 8.5 4.5 8.5s4.5-5.1 4.5-8.5A4.5 4.5 0 0 0 13 6.5z" fill="none" stroke="#fff" stroke-width="1.6"/><circle cx="13" cy="11" r="1.6" fill="#fff"/></svg>Tauranga, New Zealand's<br>North Island</li>
      <li class="contact-item"><svg viewBox="0 0 26 26"><circle cx="13" cy="13" r="11" fill="none" stroke="#fff" stroke-width="1.6"/><rect x="7.5" y="9" width="11" height="8" rx="1" fill="#fff"/><path d="M7.5 9.5l5.5 4 5.5-4" fill="none" stroke="#033d52" stroke-width="1.2"/></svg>clara@marlowhire.nz</li>
      <li class="contact-item"><svg viewBox="0 0 26 26"><circle cx="13" cy="13" r="11" fill="none" stroke="#fff" stroke-width="1.6"/><circle cx="13" cy="13" r="6" fill="none" stroke="#fff" stroke-width="1.3"/><path d="M7 13h12M13 7c-2.5 3-2.5 9 0 12M13 7c2.5 3 2.5 9 0 12" fill="none" stroke="#fff" stroke-width="1.1"/></svg>www.marlowhire.nz</li>
    </ul>
  </article>
</section>

<article class="card" style="left:381px; top:979px;">
  <div class="front-halo"></div>
  <div class="front-name">Marlow Hire</div>
  <div class="front-web">www.marlowhire.nz</div>
</article>

<article class="card" style="left:381px; top:1771px;">
  <div class="back-top"></div>
  <div class="back-mark">Marlow<br>Hire</div>
  <div class="holder-name">Clara Whitfield</div>
  <div class="holder-role">Director | Senior Search Consultant</div>
  <div class="divider"></div>
  <span class="social social--one"></span><span class="social social--two"></span>
  <ul class="contact-list">
    <li class="contact-item"><svg viewBox="0 0 26 26"><circle cx="13" cy="13" r="11" fill="none" stroke="#fff" stroke-width="1.6"/><path d="M9 8l2 0 1 3-1.3 1a6 6 0 0 0 3 3l1-1.3 3 1v2a1.5 1.5 0 0 1-1.6 1.4A9 9 0 0 1 7.7 9.6 1.5 1.5 0 0 1 9 8z" fill="#fff"/></svg>+64 27 555 0142</li>
    <li class="contact-item"><svg viewBox="0 0 26 26"><circle cx="13" cy="13" r="11" fill="none" stroke="#fff" stroke-width="1.6"/><path d="M13 6.5a4.5 4.5 0 0 0-4.5 4.5c0 3.4 4.5 8.5 4.5 8.5s4.5-5.1 4.5-8.5A4.5 4.5 0 0 0 13 6.5z" fill="none" stroke="#fff" stroke-width="1.6"/><circle cx="13" cy="11" r="1.6" fill="#fff"/></svg>Tauranga, New Zealand's<br>North Island</li>
    <li class="contact-item"><svg viewBox="0 0 26 26"><circle cx="13" cy="13" r="11" fill="none" stroke="#fff" stroke-width="1.6"/><rect x="7.5" y="9" width="11" height="8" rx="1" fill="#fff"/><path d="M7.5 9.5l5.5 4 5.5-4" fill="none" stroke="#033d52" stroke-width="1.2"/></svg>clara@marlowhire.nz</li>
    <li class="contact-item"><svg viewBox="0 0 26 26"><circle cx="13" cy="13" r="11" fill="none" stroke="#fff" stroke-width="1.6"/><circle cx="13" cy="13" r="6" fill="none" stroke="#fff" stroke-width="1.3"/><path d="M7 13h12M13 7c-2.5 3-2.5 9 0 12M13 7c2.5 3 2.5 9 0 12" fill="none" stroke="#fff" stroke-width="1.1"/></svg>www.marlowhire.nz</li>
  </ul>
</article>

</body>
</html>
```